Dog grooming business card
This is a business card for m dog grooming business like it say above.
In the priorities box below I will have the text that I want on the card.

Industry/Entity Type

Business

Colors

Designer to choose colors to be used in the design.

Requirements
Must have
• My logo and the insurance stamp must be on the card.

Text it must have :

Professional grooming services
Email: lunabrisk@mailvane.net
Text or call 1 705 318 6642
TKV certified/member
Pet first aid certified
Next appointment ___________________________________
Nice to have
• Greens to match my logo

```html
<!DOCTYPE html>
<html lang="en">
<head>
<meta charset="utf-8">
<title>Luna Brisk Dog Grooming – Business Card</title>
<link rel="stylesheet" href="https://fonts.googleapis.com/css2?family=Open+Sans:wght@400;600&display=swap">
<style>
  :root {
    --page: #ffffff;
    --brand-red: #ee1c24;
    --panel-lilac: #cdc3cb;
    --ink: #111111;
    --lime: #9bdc3c;
    --lime-deep: #2f7a1c;
    --dog-tan: #c98a4b;
    --badge-blue: #2b62b8;
  }
  html, body {
    margin: 0;
    padding: 0;
    width: 1200px;
    height: 673px;
    overflow: hidden;
    background: var(--page);
    font-family: "Open Sans", Arial, sans-serif;
    color: var(--ink);
  }
  .card {
    position: absolute;
    left: 0;
    top: 0;
    width: 1046px;
    height: 664px;
    border-right: 2px solid var(--ink);
    border-bottom: 2px solid var(--ink);
    background: var(--panel-lilac);
    overflow: hidden;
  }
  .header-band {
    position: absolute;
    left: 0;
    top: 0;
    width: 100%;
    height: 372px;
    background: var(--brand-red);
  }
  .mascot-art {
    position: absolute;
    left: 14px;
    top: 12px;
    width: 132px;
    height: 192px;
    border-radius: 40px 40px 30px 30px;
    background: radial-gradient(circle at 50% 40%, #e2a866 0%, var(--dog-tan) 60%, #a8693a 100%);
  }
  .brand-mark {
    position: absolute;
    left: 270px;
    top: 70px;
    width: 440px;
    display: flex;
    align-items: center;
    justify-content: center;
    gap: 18px;
  }
  .brand-dot {
    width: 54px;
    height: 54px;
    border-radius: 50%;
    background: var(--lime);
  }
  .brand-name {
    font-size: 64px;
    font-weight: 600;
    color: var(--lime);
    line-height: 1;
    white-space: nowrap;
  }
  .service-title {
    position: absolute;
    left: 0;
    width: 1046px;
    top: 208px;
    margin: 0;
    text-align: center;
    font-size: 148px;
    font-weight: 600;
    letter-spacing: -4px;
    line-height: 1;
    white-space: nowrap;
  }
  .credentials {
    position: absolute;
    left: 42px;
    top: 392px;
    margin: 0;
    padding: 0;
    list-style: none;
    font-size: 26px;
  }
  .credentials li {
    display: flex;
    align-items: baseline;
    height: 48px;
  }
  .credentials .label { white-space: nowrap; }
  .credentials .fill-line {
    display: inline-block;
    border-bottom: 3px dotted var(--ink);
    margin-left: 12px;
  }
  .credentials .first .fill-line { width: 490px; }
  .credentials .second .fill-line { width: 500px; }
  .credentials .third .fill-line { width: 520px; }
  .insurance-badge {
    position: absolute;
    left: 12px;
    top: 548px;
    width: 192px;
    height: 116px;
    background: #ffffff;
  }
  .insurance-badge svg { display: block; }
  .mini-brand {
    position: absolute;
    left: 222px;
    top: 548px;
    width: 202px;
    height: 108px;
    background: #ffffff;
    display: flex;
    align-items: center;
    justify-content: center;
    gap: 8px;
  }
  .mini-brand .brand-dot { width: 22px; height: 22px; }
  .mini-brand .brand-name { font-size: 26px; color: var(--lime-deep); }
  .contact {
    position: absolute;
    left: 570px;
    top: 540px;
  }
  .contact .tagline {
    margin: 0 0 4px;
    font-size: 32px;
    font-weight: 400;
    line-height: 1.2;
  }
  .contact p {
    margin: 0;
    font-size: 25px;
    line-height: 1.45;
  }
</style>
</head>
<body>
  <main class="card">
    <div class="header-band"></div>
    <div class="mascot-art" role="img" aria-label="Cartoon puppy mascot holding a red heart"></div>
    <div class="brand-mark">
      <span class="brand-dot"></span>
      <span class="brand-name">Luna Brisk</span>
    </div>
    <h1 class="service-title">Dog grooming</h1>

    <ul class="credentials">
      <li class="first"><span class="label">TKV certified/Member</span><span class="fill-line"></span></li>
      <li class="second"><span class="label">Pet first aid certified</span><span class="fill-line"></span></li>
      <li class="third"><span class="label">Next appointment</span><span class="fill-line"></span></li>
    </ul>

    <div class="insurance-badge" role="img" aria-label="Insurance protection badge">
      <svg width="192" height="116" viewBox="0 0 192 116">
        <rect x="22" y="30" width="148" height="70" rx="14" fill="var(--badge-blue)"/>
      </svg>
    </div>
    <div class="mini-brand">
      <span class="brand-dot"></span>
      <span class="brand-name">Luna Brisk</span>
    </div>

    <section class="contact">
      <h2 class="tagline">Professional grooming services</h2>
      <p>Email: lunabrisk@mailvane.net</p>
      <p>Text or call 1 705 318 6642</p>
    </section>
  </main>
</body>
</html>
```